Business card design needed

Our modern electrical contracting company requires business card design utilising our logo and incorporating our tag line "Service when you need it". We specialise in assisting our customers 24/7 offering a breakdown service.

Industry/Entity Type

Electrical

Contact Information for Business Card

Marcus Penfold, Electrical contractor,Tel: (08) 8546 3071, Fax: (08) 8679 4305, Mob 0428 736 514, Email: marcus.penfold@brightwirepower.com.au, Web: www.brightwirepower.com.au

Requirements
Must have
• we require a 2 sided card.
Front- Logo, tag line and contact information.
Rear- service when you need it! Call now for our 24/7 breakdown service

```html
<!DOCTYPE html>
<html lang="en">
<head>
<meta charset="utf-8">
<title>Brightwire Power Business Card</title>
<link rel="stylesheet" href="https://fonts.googleapis.com/css2?family=Anton&family=Ubuntu:wght@400;500;700&display=swap">
<style>
  :root {
    --page-bg: #e8e9eb;
    --card-white: #ffffff;
    --brand-blue: #1f55b8;
    --brand-blue-light: #4f8fe0;
    --brand-navy: #0f3a8c;
    --band-dark: #2a2a2a;
    --band-light: #9a9a9a;
    --ink-black: #111111;
    --text-white: #ffffff;
  }
  html, body {
    margin: 0;
    width: 1200px;
    height: 861px;
    overflow: hidden;
    background: var(--page-bg);
  }
  .card-stage {
    position: relative;
    width: 1200px;
    height: 861px;
  }
  .business-card {
    position: absolute;
    top: 285px;
    width: 510px;
    height: 296px;
    background: var(--card-white);
    box-shadow: 0 6px 18px rgba(0,0,0,0.18);
  }
  .business-card--rear { left: 60px; }
  .business-card--front { left: 630px; }
  .business-card svg { display: block; width: 100%; height: 100%; }
  .brand-name { font-family: "Ubuntu", sans-serif; font-weight: 700; fill: var(--brand-blue); }
  .tagline { font-family: "Anton", sans-serif; fill: var(--ink-black); letter-spacing: 0.2px; }
  .call-to-action { font-family: "Ubuntu", sans-serif; font-weight: 500; fill: var(--brand-blue); }
  .holder-line { font-family: "Ubuntu", sans-serif; font-weight: 700; fill: var(--text-white); }
  .contact-line { font-family: "Ubuntu", sans-serif; font-weight: 400; fill: var(--text-white); }
  .contact-label { font-weight: 500; }
</style>
</head>
<body>
<main class="card-stage">

  <section class="business-card business-card--rear" aria-label="Card rear">
    <svg viewBox="0 0 500 290" preserveAspectRatio="none">
      <defs>
        <linearGradient id="rearBlue" x1="0" y1="0" x2="1" y2="1">
          <stop offset="0" stop-color="var(--brand-blue-light)"/>
          <stop offset="1" stop-color="var(--brand-blue)"/>
        </linearGradient>
        <linearGradient id="rearBand" x1="1" y1="1" x2="0.4" y2="0.3">
          <stop offset="0" stop-color="var(--band-dark)"/>
          <stop offset="1" stop-color="var(--band-light)"/>
        </linearGradient>
      </defs>
      <polygon class="corner-band" points="0,0 230,0 0,122" fill="url(#rearBlue)"/>
      <polygon class="corner-notch" points="305,0 385,0 342,46" fill="var(--brand-navy)"/>
      <polygon class="corner-band" points="500,138 500,290 285,290" fill="url(#rearBand)"/>
      <polygon class="pointer-arrow" fill="#555" transform="translate(262,262) rotate(-40)"
               points="0,-30 18,-8 6,-8 6,26 -6,26 -6,-8 -18,-8"/>
      <circle class="brand-mark" cx="250" cy="58" r="32" fill="var(--brand-blue)"/>
      <text class="brand-name" x="250" y="150" font-size="29" text-anchor="middle">BRIGHTWIRE POWER</text>
      <text class="tagline" x="36" y="207" font-size="25">SERVICE WHEN YOU NEED IT!</text>
      <text class="call-to-action" x="38" y="237" font-size="18">Call now for our 24/7</text>
      <text class="call-to-action" x="38" y="264" font-size="18">breakdown service</text>
    </svg>
  </section>

  <section class="business-card business-card--front" aria-label="Card front">
    <svg viewBox="0 0 500 290" preserveAspectRatio="none">
      <defs>
        <linearGradient id="frontBlue" x1="0" y1="0" x2="1" y2="1">
          <stop offset="0" stop-color="var(--brand-blue-light)"/>
          <stop offset="1" stop-color="var(--brand-blue)"/>
        </linearGradient>
        <linearGradient id="frontBand" x1="0.3" y1="0.4" x2="1" y2="1">
          <stop offset="0" stop-color="var(--band-dark)"/>
          <stop offset="1" stop-color="#c4c4c4"/>
        </linearGradient>
      </defs>
      <polygon class="corner-band" points="0,0 220,0 0,125" fill="url(#frontBlue)"/>
      <polygon class="corner-notch" points="298,0 378,0 338,40" fill="var(--brand-navy)"/>
      <polygon class="diagonal-band" points="500,15 500,290 40,290" fill="url(#frontBand)"/>
      <polygon class="pointer-arrow" fill="#666" transform="translate(468,44) rotate(-60)"
               points="0,-26 16,-8 6,-8 6,22 -6,22 -6,-8 -16,-8"/>
      <polygon class="pointer-arrow" fill="#ffffff" transform="translate(262,258)"
               points="0,-30 17,-10 6,-10 6,26 -6,26 -6,-10 -17,-10"/>
      <circle class="brand-mark" cx="160" cy="118" r="30" fill="var(--brand-blue)"/>
      <text class="brand-name" font-size="26" transform="translate(62,268) rotate(-31)">BRIGHTWIRE POWER</text>
      <text class="holder-line" font-size="16" transform="translate(106,282) rotate(-31)">MARCUS PENFOLD • Electrical contractor</text>
      <g class="contact-block" font-size="9.5">
        <text class="contact-line" transform="translate(273.3,201.3) rotate(-31)"><tspan class="contact-label">Telephone:</tspan> (08) 8546 3071</text>
        <text class="contact-line" transform="translate(280,212.4) rotate(-31)"><tspan class="contact-label">Fax:</tspan> (08) 8679 4305</text>
        <text class="contact-line" transform="translate(286.6,223.6) rotate(-31)"><tspan class="contact-label">Mobile:</tspan> 0428 736 514</text>
        <text class="contact-line" transform="translate(293.3,234.7) rotate(-31)"><tspan class="contact-label">Email:</tspan> marcus.penfold@brightwirepower.com.au</text>
        <text class="contact-line" transform="translate(300,245.8) rotate(-31)"><tspan class="contact-label">Website:</tspan> www.brightwirepower.com.au</text>
      </g>
    </svg>
  </section>

</main>
</body>
</html>
```